Website for Cuff-Tastics
Cuff-Tastics
Project: Website for Cuff-Tastics
Website for Cuff-Tastics - Retailers
Creative Brief
Retailers
Cuff-Tastics.com (pending)
The ‘Perfect Little Black Dress’.  You know when you've found it – chic, elegant, stylish and flattering! What’s not perfect is that sexy LBD’s are made for the mythical woman, the woman with toned, smooth, perfect arms. Dieting, exercise, lifting weights, toddlers and groceries and still perfection eludes us. Being a mere mortal means that changes in skin tone and muscle are inevitable. What to do? Stylish, little numbers can leave you feeling too exposed for comfort.  Dresses with sleeves are often matronly and dowdy. After years of heroic home-lab research and clumsy attempts using pantyhose as sleeves, I had a moment of pure inspiration! What women needed were flattering, interchangeable sleeves without costly, permanent dress alterations. Cuff-tastics was born. Cuff-tastics instantly make the perfect sleeveless LBD wearable by real women with real arms. That one perfect LBD is transformed into two, three, four or more little black dresses. You’re ready for a first date, a party, and a special gala event without extra effort or expense. Made from comfortable, breathable stretch fabric, Cuff-tastics are laser-cut, seamless camisoles with an array of flattering sleeve choices including mesh, lace, chiffon, fitted, and flutter three-quarters. They will become a seamless part of your wardrobe, transforming everything you own. It’s no myth that women of all ages can feel vibrant, energized, and youthful-and they can look that way too.  The key is to embrace who we are and use all the tools available to look our best and feel confident.  Cuff-tastics are sure to be an essential component of your wardrobe. We’ve earned the right to “bare” arms but we may choose not to!
Like a clean look with white space. Like prominent images. Dislike busy-ness. THE IMAGES FOR THE WEBSITE THAT WE WANT CAN BE SEEN HERE: http://qx.zp/8kTRwbnL47
black
Blue used in Logo
above header
http://www.plumerido.com/
http://www.trivok.com/
http://www.cardelune.com/
We'll forward a pdf file with content and a suggested layout. We will upgrade to a commerce site within 3 months. THE IMAGES FOR THE WEBSITE THAT WE WANT CAN BE SEEN HERE: http://qx.zp/8kTRwbnL47

```html
<!DOCTYPE html>
<html lang="en">
<head>
<meta charset="utf-8">
<title>Cuff-Tastics</title>
<link href="https://fonts.googleapis.com/css2?family=Source+Sans+3:wght@400;600;700;900&display=swap" rel="stylesheet">
<style>
  :root {
    --page: #ffffff;
    --backdrop: #f2f2f2;
    --ink: #222222;
    --grey: #7a7a7a;
    --light-grey: #a8a8a8;
    --teal: #3f8f9c;
    --teal-dark: #2a6f82;
    --accent-red: #c2312c;
    --cta: #f0a262;
    --rule: #d9d9d9;
  }
  * { box-sizing: border-box; margin: 0; padding: 0; }
  html, body { width: 1200px; height: 715px; overflow: hidden; background: var(--backdrop); }
  body { font-family: "Source Sans 3", "Helvetica Neue", Arial, sans-serif; color: var(--ink); position: relative; }

  .side-photo { position: absolute; top: 0; height: 560px; }
  .side-photo.left { left: 0; width: 160px; background: linear-gradient(90deg, #d8d8d8, #bdbdbd 45%, #e9e9e9); }
  .side-photo.right { right: 0; width: 156px; background: linear-gradient(90deg, #e9e9e9, #b9b9b9 55%, #d6d6d6); }

  .page { position: absolute; left: 160px; top: 0; width: 884px; height: 715px; background: var(--page); }

  .brand { position: absolute; left: 32px; top: 0; width: 168px; height: 120px; display: flex; flex-direction: column; align-items: center; justify-content: center; gap: 10px; }
  .brand-mark { width: 56px; height: 56px; background: var(--teal); }
  .brand-name { font-size: 15px; font-weight: 600; letter-spacing: 1px; color: var(--ink); }

  .account-links { position: absolute; right: 84px; top: 29px; display: flex; gap: 14px; font-size: 11px; color: var(--grey); }

  .main-nav { position: absolute; right: 80px; top: 104px; display: flex; font-size: 13px; letter-spacing: .5px; }
  .main-nav a { padding: 0 10px; color: var(--grey); text-decoration: none; border-left: 1px solid var(--rule); line-height: 22px; }
  .main-nav a:first-child { border-left: 0; }
  .main-nav a.current { color: var(--ink); font-weight: 700; }

  .hero-photo { position: absolute; left: 536px; top: 144px; width: 348px; height: 413px; background: radial-gradient(ellipse at 50% 40%, #d9a88a 0%, #b27a5e 25%, #2d6f73 55%, #e8e8e8 90%, #ffffff 100%); }

  .pitch { position: absolute; left: 27px; top: 230px; width: 490px; color: var(--grey); font-size: 16px; line-height: 1.35; }
  .pitch p { margin-bottom: 14px; }
  .pitch .big { font-size: 22px; }
  .pitch .black { color: var(--ink); font-weight: 900; font-size: 27px; }
  .pitch .red { color: var(--accent-red); font-weight: 700; font-size: 20px; }
  .pitch .strong { color: var(--ink); font-weight: 600; }
  .pitch .teal { color: var(--teal-dark); font-weight: 700; font-size: 27px; }
  .pitch .heavy { color: var(--light-grey); font-weight: 900; font-size: 26px; letter-spacing: .5px; }
  .pitch .indent1 { padding-left: 70px; }
  .pitch .indent2 { padding-left: 150px; }
  .pitch .indent3 { padding-left: 230px; }

  .cta { position: absolute; left: 204px; top: 506px; font-size: 21px; color: var(--cta); text-decoration: none; letter-spacing: .5px; border-bottom: 1px solid var(--cta); }

  .footer-rule { position: absolute; left: 32px; right: 32px; top: 612px; border-top: 1px solid var(--rule); }
  .social { position: absolute; left: 32px; top: 622px; display: flex; gap: 4px; }
  .social span { width: 16px; height: 16px; background: #9a9a9a; display: block; }
  .footer-nav { position: absolute; right: 80px; top: 622px; display: flex; gap: 16px; font-size: 12px; color: var(--grey); letter-spacing: .3px; }
  .footer-nav .current { color: var(--ink); font-weight: 700; }
  .copyright { position: absolute; left: 32px; top: 664px; font-size: 11px; color: var(--ink); }
</style>
</head>
<body>
  <div class="side-photo left" role="img" aria-label="Photo of a woman in a black dress with lace sleeves, standing"></div>
  <div class="side-photo right" role="img" aria-label="Photo of a woman in a black dress with sheer sleeves, standing"></div>

  <main class="page">
    <header>
      <div class="brand"><span class="brand-mark"></span><span class="brand-name">CUFF-TASTICS</span></div>
      <nav class="account-links"><span>My Account</span><span>My Cart</span><span>Checkout</span><span>Log In</span></nav>
      <nav class="main-nav">
        <a class="current" href="#">THE PROBLEM</a><a href="#">THE SO-LUTION</a><a href="#">THE COLLECTION</a><a href="#">ABOUT US</a><a href="#">CONTACT US</a>
      </nav>
    </header>

    <div class="hero-photo" role="img" aria-label="Portrait of a smiling red-haired woman in a teal dress with black lace sleeves"></div>

    <section class="pitch">
      <p>The <span class="big">‘Perfect Little <span class="black">Black</span> Dress’</span>? Almost perfect … but sleeveless.<br>
      <span class="indent1">Why is that all those <span class="red">sexy LBDs</span> are made for <span class="strong">women</span></span><br>
      <span class="indent2">with <span class="strong">toned, smooth, arms</span>?</span></p>
      <p>Even after <span class="strong">dieting, exercising</span> and lifting weights, toddlers, and groceries,<br>
      <span class="indent2">those <span class="strong">svelte arms</span> seem to <span class="teal">elude us.</span></span></p>
      <p><span class="strong">Dresses</span> with <span class="strong">sleeves</span> are often matronly and dowdy.<br>
      <span class="indent1"><span class="strong" style="color:var(--teal-dark)">Stylish</span>, little numbers can leave you feeling</span><br>
      <span class="heavy">too exposed</span> for <span class="strong">comfort.</span></p>
    </section>

    <a class="cta" href="#">CLICK TO SEE COLLECTION</a>

    <footer>
      <div class="footer-rule"></div>
      <div class="social"><span></span><span></span><span></span></div>
      <nav class="footer-nav"><span class="current">THE PROBLEM</span><span>THE SO-LUTION</span><span>THE COLLECTION</span><span>ABOUT US</span><span>CONTACT US</span></nav>
      <p class="copyright">Copyright © 2013 Cuff-Tastics. All Rights Reserved.</p>
    </footer>
  </main>
</body>
</html>
```